Tr construction holdings pty ltd

2 sided card black and red with white
Very professional and elegant

Target Market(s)

Construction and Development

Industry/Entity Type

Construction and development

Contact Information for Business Card

One side black, one side red/or white business logo in top corner, email: morgan@trbuildworks.example

Requirements
Should not have
• Blue

```html
<!DOCTYPE html>
<html lang="en">
<head>
<meta charset="UTF-8">
<title>Tr Construction Holdings – Business Card</title>
<link rel="stylesheet" href="https://fonts.googleapis.com/css2?family=Montserrat:wght@500;600&family=Open+Sans:wght@400;600&display=swap">
<style>
  :root {
    --backdrop: #3a3a3b;
    --card: #232324;
    --card-back: #262627;
    --ink: #ffffff;
    --accent: #e8432e;
    --emboss: #4b4b4d;
  }
  * { margin: 0; padding: 0; box-sizing: border-box; }
  html, body {
    width: 1200px;
    height: 900px;
    overflow: hidden;
    background: var(--backdrop);
  }
  .canvas {
    position: relative;
    width: 1200px;
    height: 900px;
  }
  .card {
    position: absolute;
    left: 280px;
    width: 640px;
    height: 366px;
    box-shadow: 0 14px 30px rgba(0,0,0,0.45);
  }
  .card--back {
    top: 56px;
    background: var(--card-back);
    display: flex;
    align-items: center;
    justify-content: center;
  }
  .card--front {
    top: 470px;
    background: var(--card);
    color: var(--ink);
  }
  .brand {
    display: flex;
    align-items: center;
    gap: 10px;
    font-family: "Montserrat", sans-serif;
    font-weight: 600;
    text-transform: uppercase;
    letter-spacing: 2px;
  }
  .brand__mark {
    width: 10px;
    height: 10px;
    background: var(--accent);
  }
  .card--back .brand {
    font-size: 30px;
    color: var(--emboss);
  }
  .card--back .brand__mark { background: var(--emboss); width: 14px; height: 14px; }
  .card--front .brand {
    position: absolute;
    left: 56px;
    top: 62px;
    font-size: 22px;
    color: var(--ink);
  }
  .address {
    position: absolute;
    left: 60px;
    top: 150px;
    font-family: "Open Sans", sans-serif;
    font-size: 15px;
    line-height: 24px;
    letter-spacing: 0.8px;
  }
  .contact-list {
    position: absolute;
    left: 56px;
    top: 214px;
    list-style: none;
    font-family: "Open Sans", sans-serif;
    font-size: 15px;
    letter-spacing: 0.8px;
  }
  .contact-list li {
    display: flex;
    align-items: center;
    gap: 10px;
    height: 26px;
  }
  .contact-list svg { width: 15px; height: 15px; fill: var(--accent); flex: none; }
  .person {
    position: absolute;
    right: 54px;
    top: 238px;
    text-align: right;
  }
  .person__name {
    font-family: "Montserrat", sans-serif;
    font-weight: 500;
    font-size: 25px;
    letter-spacing: 2.5px;
    text-transform: uppercase;
  }
  .person__surname { color: var(--accent); }
  .person__role {
    font-family: "Open Sans", sans-serif;
    font-size: 15px;
    letter-spacing: 1px;
    margin-top: 4px;
  }
  .accent-bar {
    position: absolute;
    right: 24px;
    top: 262px;
    width: 14px;
    height: 56px;
    background: var(--accent);
  }
</style>
</head>
<body>
<main class="canvas">
  <section class="card card--back" aria-label="Card back">
    <div class="brand"><span class="brand__mark"></span><span>Tr Construction Holdings</span></div>
  </section>

  <section class="card card--front" aria-label="Card front">
    <div class="brand"><span>Tr Construction Holdings</span><span class="brand__mark"></span></div>

    <p class="address">P.O. Box 000. Postal Code 00<br>Your City, Country</p>

    <ul class="contact-list">
      <li>
        <svg viewBox="0 0 24 24" aria-hidden="true"><path d="M6.6 10.8a15.1 15.1 0 0 0 6.6 6.6l2.2-2.2c.3-.3.7-.4 1-.2 1.1.4 2.3.6 3.6.6.6 0 1 .4 1 1V20c0 .6-.4 1-1 1A17 17 0 0 1 3 4c0-.6.4-1 1-1h3.5c.6 0 1 .4 1 1 0 1.3.2 2.5.6 3.6.1.3 0 .7-.2 1z"/></svg>
        <span>(123)456-7891</span>
      </li>
      <li>
        <svg viewBox="0 0 24 24" aria-hidden="true"><path d="M2 5h20v14H2z M2 5l10 8 10-8" /></svg>
        <span>morgan@trbuildworks.example</span>
      </li>
      <li>
        <svg viewBox="0 0 24 24" aria-hidden="true"><circle cx="12" cy="12" r="10"/></svg>
        <span>www.trbuildworks.example</span>
      </li>
    </ul>

    <div class="person">
      <p class="person__name">John <span class="person__surname">Smith</span></p>
      <p class="person__role">Director</p>
    </div>
    <div class="accent-bar"></div>
  </section>
</main>
</body>
</html>
```